VALMIRA/ VALMIRA GREY Business Card

We have two brands that we would like to show one 1 business card (front and back). We would to incorporate two different logos on one card (VALMIRA and VALMIRA GREY). Card can be two sided. Simple, sleek and professional.

We are a senior living provider.

www.valmira-example.com
www.valmiragrey-example.com

Target Market(s)

Professionals

Industry/Entity Type

Business

Font styles to use
Serif

Colors

Designer to choose colors to be used in the design.

Requirements
Must have
• Space for EMAIL, PHONE, WEBSITE
Nice to have
• Raised lettering or gloss lettering

```html
<!DOCTYPE html>
<html lang="en">
<head>
<meta charset="UTF-8">
<title>Valmira / Valmira Grey Business Card</title>
<link href="https://fonts.googleapis.com/css2?family=Bebas+Neue&family=Cinzel:wght@500&family=Open+Sans:wght@400&display=swap" rel="stylesheet">
<style>
  :root {
    --backdrop: #8b8b8b;
    --card: #262626;
    --gold: #c6962b;
    --silver: #e6e6e6;
    --text-light: #dcdcdc;
  }
  html, body {
    margin: 0;
    padding: 0;
    width: 1200px;
    height: 781px;
    overflow: hidden;
    background: var(--backdrop);
  }
  .canvas {
    position: relative;
    width: 1200px;
    height: 781px;
  }
  .card {
    position: absolute;
    left: 358px;
    width: 454px;
    height: 251px;
    background: var(--card);
  }
  .card--front { top: 103px; }
  .card--back { top: 410px; }

  .holder {
    position: absolute;
    right: 242px;
    top: 102px;
    text-align: right;
  }
  .holder-name {
    font-family: "Bebas Neue", sans-serif;
    font-size: 34px;
    line-height: 1;
    letter-spacing: 0.5px;
    color: var(--silver);
    margin: 0;
  }
  .holder-role {
    font-family: "Open Sans", sans-serif;
    font-size: 11.5px;
    color: var(--text-light);
    margin: 2px 0 0;
  }
  .divider {
    position: absolute;
    left: 227px;
    top: 101px;
    width: 1px;
    height: 52px;
    background: var(--text-light);
  }
  .contact-list {
    position: absolute;
    left: 241px;
    top: 98px;
    margin: 0;
    padding: 0;
    list-style: none;
  }
  .contact-item {
    display: flex;
    align-items: center;
    height: 15px;
    font-family: "Open Sans", sans-serif;
    font-size: 11.5px;
    color: var(--text-light);
  }
  .contact-icon {
    width: 9px;
    height: 9px;
    margin-right: 7px;
    flex: none;
  }
  .address {
    position: absolute;
    left: 0;
    right: 0;
    top: 223px;
    text-align: center;
    font-family: "Open Sans", sans-serif;
    font-size: 11.5px;
    color: var(--text-light);
    margin: 0;
  }

  .brand-primary {
    position: absolute;
    left: 0;
    right: 0;
    top: 68px;
    display: flex;
    justify-content: center;
    align-items: center;
    gap: 10px;
  }
  .brand-mark {
    width: 26px;
    height: 26px;
    background: var(--gold);
  }
  .brand-primary-name {
    font-family: "Cinzel", serif;
    font-weight: 500;
    font-size: 38px;
    line-height: 1;
    color: var(--gold);
    letter-spacing: 1px;
  }
  .brand-secondary {
    position: absolute;
    left: 0;
    right: 0;
    top: 152px;
    text-align: center;
  }
  .brand-secondary-name {
    font-family: "Cinzel", serif;
    font-weight: 500;
    font-size: 23px;
    line-height: 1;
    color: var(--silver);
    letter-spacing: 0.5px;
    margin: 0;
  }
  .brand-tagline {
    font-family: "Open Sans", sans-serif;
    font-size: 11.5px;
    color: var(--text-light);
    margin: 3px 0 0;
  }
</style>
</head>
<body>
<div class="canvas">

  <section class="card card--front">
    <div class="holder">
      <p class="holder-name">CLARA NOVAK</p>
      <p class="holder-role">Manager</p>
    </div>
    <div class="divider"></div>
    <ul class="contact-list">
      <li class="contact-item">
        <svg class="contact-icon" viewBox="0 0 10 10"><path d="M2 1 L4 1 L4.6 3 L3.4 3.8 Q4.4 5.8 6.2 6.6 L7 5.4 L9 6 L9 8 Q9 9 8 9 Q1 8.5 1 2 Q1 1 2 1Z" fill="none" stroke="#c6962b" stroke-width="1"/></svg>
        +000 555 0142
      </li>
      <li class="contact-item">
        <svg class="contact-icon" viewBox="0 0 10 10"><rect x="0.5" y="2" width="9" height="6.5" fill="#c6962b"/><path d="M0.5 2 L5 5.5 L9.5 2" fill="none" stroke="#262626" stroke-width="0.9"/></svg>
        info@valmira-example.com
      </li>
      <li class="contact-item">
        <svg class="contact-icon" viewBox="0 0 10 10"><circle cx="5" cy="5" r="4.3" fill="none" stroke="#c6962b" stroke-width="1"/><ellipse cx="5" cy="5" rx="1.8" ry="4.3" fill="none" stroke="#c6962b" stroke-width="0.8"/><line x1="0.7" y1="5" x2="9.3" y2="5" stroke="#c6962b" stroke-width="0.8"/></svg>
        www.valmira-example.com
      </li>
      <li class="contact-item">
        <svg class="contact-icon" viewBox="0 0 10 10"><circle cx="5" cy="5" r="4.3" fill="none" stroke="#c6962b" stroke-width="1"/><ellipse cx="5" cy="5" rx="1.8" ry="4.3" fill="none" stroke="#c6962b" stroke-width="0.8"/><line x1="0.7" y1="5" x2="9.3" y2="5" stroke="#c6962b" stroke-width="0.8"/></svg>
        www.valmiragrey-example.com
      </li>
    </ul>
    <p class="address">12 Harbor Lane, Westbrook Avenue, Lakeside, CA 000000</p>
  </section>

  <section class="card card--back">
    <div class="brand-primary">
      <span class="brand-mark"></span>
      <span class="brand-primary-name">VALMIRA</span>
    </div>
    <div class="brand-secondary">
      <p class="brand-secondary-name">VALMIRA GREY</p>
      <p class="brand-tagline">Executive Personal Care Services</p>
    </div>
  </section>

</div>
</body>
</html>
```